Verdant Medispa Business Card

need a business card for our medispa, attached please see the logo.
our website is https://verdantmedispa-example.com

Sorina Belcourt, MD
Internal Medicine

555-204-7193

Sorina@verdantmedispa-example.com

Www.Verdantmedispa-example.com

738 E Harlow Blvd N, Ste 512, Katy, TX 77981

Target Market(s)

MedSpa, Cosmetics, Esthetics

Industry/Entity Type

MedicalSpa

Contact Information for Business Card

Please see the attached business card which i pulled from the internet. I like the idea back as a logo and front with info.

Font styles to use
Decorative

Requirements
Must have
• Color should be matching with Logo and Website theme, Also I like to have QR code for the website

```html
<!DOCTYPE html>
<html lang="en">
<head>
<meta charset="utf-8">
<title>Verdant MediSpa – Business Card</title>
<link rel="stylesheet" href="https://fonts.googleapis.com/css2?family=Cormorant+Garamond:wght@600;700&family=Montserrat:wght@400;500&display=swap">
<style>
  :root {
    --backdrop: #222822;
    --card-white: #ffffff;
    --gold: #c9a227;
    --gold-light: #e2c24a;
    --ink-brown: #44342a;
    --text-brown: #3d3028;
    --back-light: #7a6252;
    --back-dark: #55443a;
    --white: #ffffff;
  }
  * { margin: 0; padding: 0; box-sizing: border-box; }
  html, body {
    width: 1200px;
    height: 1200px;
    overflow: hidden;
    background: var(--backdrop);
  }
  .card {
    position: absolute;
    left: 240px;
    width: 728px;
    height: 415px;
    border-radius: 25px;
    overflow: hidden;
    text-align: center;
  }
  .card--front { top: 141px; background: var(--card-white); }
  .card--back {
    top: 648px;
    background: linear-gradient(60deg, var(--back-light) 0%, var(--back-dark) 100%);
  }

  .brand-name {
    position: absolute;
    left: 0;
    width: 100%;
    font-family: "Cormorant Garamond", serif;
    font-weight: 600;
    line-height: 1;
  }
  .card--front .brand-name { top: 52px; color: var(--gold); }
  .card--back .brand-name { top: 150px; color: var(--white); }
  .brand-name__main { display: block; }
  .card--front .brand-name__main { font-size: 62px; }
  .card--back .brand-name__main { font-size: 86px; }
  .brand-name__sub {
    display: block;
    letter-spacing: 0.35em;
    padding-left: 0.35em;
  }
  .card--front .brand-name__sub { font-size: 20px; margin-top: 8px; }
  .card--back .brand-name__sub { font-size: 28px; margin-top: 14px; }

  .person-name {
    position: absolute;
    top: 196px;
    left: 0;
    width: 100%;
    font-family: "Cormorant Garamond", serif;
    font-weight: 700;
    font-size: 44px;
    letter-spacing: 0.01em;
    color: var(--ink-brown);
  }
  .person-role {
    position: absolute;
    top: 250px;
    left: 0;
    width: 100%;
    font-family: "Montserrat", sans-serif;
    font-size: 20px;
    letter-spacing: 0.12em;
    color: var(--gold);
  }
  .contact-divider {
    position: absolute;
    top: 278px;
    left: 146px;
    width: 437px;
    height: 24px;
  }
  .contact-list {
    position: absolute;
    top: 310px;
    left: 0;
    width: 100%;
    list-style: none;
    font-family: "Montserrat", sans-serif;
    font-size: 19px;
    line-height: 29px;
    color: var(--text-brown);
  }
  .website {
    position: absolute;
    top: 306px;
    left: 0;
    width: 100%;
    font-family: "Montserrat", sans-serif;
    font-size: 21px;
    letter-spacing: 0.1em;
    color: var(--white);
  }
</style>
</head>
<body>

  <section class="card card--front" aria-label="Business card front">
    <div class="brand-name">
      <span class="brand-name__main">Verdant</span>
      <span class="brand-name__sub">MediSpa</span>
    </div>

    <h1 class="person-name">SORINA BELCOURT, MD</h1>
    <p class="person-role">Internal Medicine</p>

    <svg class="contact-divider" viewBox="0 0 437 24" aria-hidden="true">
      <line x1="0" y1="12" x2="153" y2="12" stroke="#c9a227" stroke-width="2"/>
      <line x1="284" y1="12" x2="437" y2="12" stroke="#c9a227" stroke-width="2"/>
      <!-- phone -->
      <path d="M171 4 c-2 1 -3 3 -2 6 c1 4 4 8 7 10 c2 1 4 0 5 -1 l-3 -3 c-1 1 -2 1 -3 0 c-1 -1 -3 -4 -3 -5 c0 -1 1 -1 2 -2 z" fill="#c9a227"/>
      <!-- envelope -->
      <rect x="208" y="5" width="18" height="13" fill="#c9a227"/>
      <path d="M208 5 l9 7 l9 -7" fill="none" stroke="#ffffff" stroke-width="1.4"/>
      <!-- pin -->
      <path d="M261 2 a6.5 6.5 0 0 1 6.5 6.5 c0 5 -6.5 13 -6.5 13 c0 0 -6.5 -8 -6.5 -13 a6.5 6.5 0 0 1 6.5 -6.5 z" fill="#c9a227"/>
      <circle cx="261" cy="8.5" r="2.4" fill="#ffffff"/>
    </svg>

    <ul class="contact-list">
      <li>555-204-7193</li>
      <li>Sorina@verdantmedispa-example.com</li>
      <li>738 E Harlow Blvd N, Ste 512, Katy, TX 77981</li>
    </ul>
  </section>

  <section class="card card--back" aria-label="Business card back">
    <div class="brand-name">
      <span class="brand-name__main">Verdant</span>
      <span class="brand-name__sub">MediSpa</span>
    </div>
    <p class="website">www.verdantmedispa-example.com</p>
  </section>

</body>
</html>
```